Professional looking Roller Blind Discount Card that portrays quality at a value for money price!

We need a double sided business card designed as a discount card. Size 90mm wide x 55mm high.We would like it to look professional and portray quality at a value for money price point.I have uploaded a word document with a basic layout with the information we want included on each side of the card. Please put your own thought into the layout.

As per word document attached.

```html
<!DOCTYPE html>
<html lang="en">
<head>
<meta charset="utf-8">
<title>Roller Blinds Discount Card</title>
<link rel="stylesheet" href="https://fonts.googleapis.com/css2?family=Poppins:wght@400;500;700;800&family=Great+Vibes&display=swap">
<style>
  :root{
    --brand-blue:#29a3dc;
    --brand-blue-deep:#1b7fc4;
    --card-white:#f7f8f9;
    --ink:#3b3d40;
    --seal-grey:#3a3d42;
    --backdrop:#e4e6e9;
  }
  *{box-sizing:border-box;margin:0;padding:0}
  html,body{width:1200px;height:874px;overflow:hidden;background:var(--backdrop)}
  body{position:relative;font-family:"Poppins",sans-serif}

  .card{position:absolute;left:270px;width:660px;height:403px;background:var(--card-white);overflow:hidden;box-shadow:0 6px 18px rgba(0,0,0,.18)}
  .card--front{top:24px}
  .card--back{top:447px}

  /* front */
  .front-header{position:absolute;left:0;top:0;width:100%;height:112px;background:var(--brand-blue);color:#fff;padding:8px 26px 0}
  .front-title{font-weight:800;font-size:70px;line-height:66px;letter-spacing:-1px;white-space:nowrap}
  .front-subtitle{font-weight:500;font-size:30px;line-height:34px;margin-top:2px;white-space:nowrap}
  .front-photo{position:absolute;left:28px;top:132px;width:420px;height:232px;background:linear-gradient(100deg,#6b5a4f 0%,#7d6b5e 22%,#5f7a4c 45%,#86a36a 70%,#c9c4b6 100%)}
  .front-call{position:absolute;left:28px;top:320px;width:400px;height:44px;background:var(--brand-blue);color:#fff;font-size:22px;line-height:44px;padding-left:14px;white-space:nowrap}
  .front-call strong{font-weight:700}
  .fabric-bubble{position:absolute;left:470px;top:150px;width:170px;height:110px}
  .fabric-bubble svg{display:block}
  .fabric-bubble span{position:absolute;left:0;top:18px;width:170px;text-align:center;font-family:"Great Vibes",cursive;font-size:22px;line-height:22px;color:#fff}
  .front-brand{position:absolute;left:468px;top:322px;width:176px;display:flex;align-items:center;gap:8px;color:var(--brand-blue-deep);font-weight:700;font-size:16px;white-space:nowrap}
  .front-brand i{display:block;width:14px;height:14px;background:var(--brand-blue-deep)}

  /* back */
  .back-band{position:absolute;left:0;top:0;width:100%;height:198px;background:var(--brand-blue)}
  .offer{position:absolute;left:0;top:12px;width:100%;text-align:center;color:#fff}
  .offer-amount{font-weight:800;font-size:80px;line-height:82px}
  .offer-line{font-weight:500;font-size:27px;line-height:32px;white-space:nowrap}
  .seal{position:absolute;top:184px;width:136px;height:136px;border-radius:50%;background:radial-gradient(circle at 50% 40%,#5cc3f0 0%,#2f8fd0 55%,var(--seal-grey) 56%,var(--seal-grey) 100%)}
  .seal--free{left:80px}
  .seal--best{left:262px}
  .seal--family{left:444px}
  .back-call{position:absolute;left:0;top:334px;width:100%;text-align:center;font-size:34px;color:var(--ink);font-weight:400;white-space:nowrap}
  .back-call strong{color:var(--brand-blue);font-weight:700}
</style>
</head>
<body>

<section class="card card--front">
  <header class="front-header">
    <h1 class="front-title">ROLLER BLINDS</h1>
    <p class="front-subtitle">FREE in Home Measure &amp; Quote</p>
  </header>
  <div class="front-photo" role="img" aria-label="Photo of a room with white-framed windows looking onto a lush green garden"></div>
  <p class="front-call">CALL <strong>0400 123 456</strong> TODAY!</p>
  <div class="fabric-bubble">
    <svg width="170" height="110" viewBox="0 0 170 110" aria-hidden="true">
      <defs>
        <linearGradient id="bubble-fill" x1="0" y1="0" x2="0" y2="1">
          <stop offset="0" stop-color="#5cc3f0"/>
          <stop offset="1" stop-color="#1b7fc4"/>
        </linearGradient>
      </defs>
      <ellipse cx="85" cy="42" rx="82" ry="40" fill="url(#bubble-fill)"/>
      <path d="M40 70 L30 104 L64 78 Z" fill="#1f86c9"/>
    </svg>
    <span>Huge Selection<br>of Fabrics</span>
  </div>
  <div class="front-brand"><i></i>J&amp;M INTERIORS</div>
</section>

<section class="card card--back">
  <div class="back-band"></div>
  <div class="offer">
    <p class="offer-amount">25% OFF</p>
    <p class="offer-line">Quality Custom Made Roller Blinds</p>
    <p class="offer-line">Blockout • screen • LightFiltering</p>
  </div>

  <div class="seal seal--free" role="img" aria-label="Seal badge: Free in home measure and quote"></div>
  <div class="seal seal--best" role="img" aria-label="Seal badge: Best price guarantee"></div>
  <div class="seal seal--family" role="img" aria-label="Seal badge: Family owned and operated"></div>

  <p class="back-call">Call <strong>0400 123 456</strong> Today!</p>
</section>

</body>
</html>
```